Woman owned consulting company needs an elegant and modern business card design

I need a business card design for my new consulting company, Mara Quill Consulting. I am looking for something that is simple and elegant, but also creative and original. You can use either version of the logo that are attached. I have also included the information that needs to be featured on the business card.

Requirements
Must have
• The logo and the font type and a standard business card size. Use shades of gray/silver and or rose gold that are in the logo.
• I didn't realize that my actual logo wasn't attached. Please incorporate in the designs.
Should not have
• Colors that are different from my logo

```html
<!DOCTYPE html>
<html lang="en">
<head>
<meta charset="utf-8">
<title>Mara Quill Consulting – Business Card</title>
<link href="https://fonts.googleapis.com/css2?family=Cormorant+Garamond:wght@500;600&family=Arimo:wght@400&display=swap" rel="stylesheet">
<style>
  :root {
    --stage: #3b3b3e;
    --card: #2a2b2b;
    --card-deep: #242525;
    --silver: #f2f2f2;
    --emboss: #4a4b4c;
    --rose: #b5707a;
    --text: #f4f4f4;
  }
  * { margin: 0; padding: 0; box-sizing: border-box; }
  html, body {
    width: 1200px; height: 1200px; overflow: hidden;
    background: var(--stage);
  }
  .sheet {
    position: relative; width: 1200px; height: 1200px;
    display: flex; flex-direction: column; align-items: center; justify-content: center;
    gap: 60px;
  }
  .card {
    position: relative; width: 840px; height: 480px;
    background: var(--card); border-radius: 26px; overflow: hidden;
  }
  /* Back side */
  .card--back { display: flex; align-items: center; justify-content: center; }
  .wordmark {
    font-family: "Cormorant Garamond", serif; font-weight: 500;
    letter-spacing: 2px; line-height: 1;
  }
  .card--back .wordmark { color: var(--emboss); font-size: 62px; }
  /* Front side */
  .card--front .wordmark {
    position: absolute; right: 60px; top: 70px;
    color: var(--silver); font-size: 54px; text-align: right;
  }
  .identity {
    position: absolute; right: 72px; top: 224px; text-align: right;
  }
  .identity__name {
    font-family: "Cormorant Garamond", serif; font-weight: 600;
    font-size: 38px; letter-spacing: 1.5px; color: var(--rose); line-height: 1;
  }
  .identity__role {
    font-family: "Arimo", sans-serif; font-size: 20px; color: var(--text);
    margin-top: 8px; margin-right: 12px; letter-spacing: 0.5px;
  }
  .identity__rule {
    width: 40px; height: 2px; background: var(--rose);
    margin: 16px 0 0 auto; margin-right: 4px;
  }
  .contacts {
    position: absolute; right: 60px; top: 340px; list-style: none;
    font-family: "Arimo", sans-serif; font-size: 20px; color: var(--text);
  }
  .contacts__item {
    display: flex; align-items: center; justify-content: flex-end;
    gap: 14px; height: 34px; letter-spacing: 0.4px;
  }
  .contacts__icon { width: 22px; height: 22px; flex: none; }
</style>
</head>
<body>
<main class="sheet">
  <section class="card card--back" aria-label="Card back">
    <div class="wordmark">Mara Quill Consulting</div>
  </section>

  <section class="card card--front" aria-label="Card front">
    <div class="wordmark">Mara Quill<br>Consulting</div>

    <div class="identity">
      <div class="identity__name">MARA QUILL</div>
      <div class="identity__role">Owner</div>
      <div class="identity__rule"></div>
    </div>

    <ul class="contacts">
      <li class="contacts__item">555-013-2847
        <svg class="contacts__icon" viewBox="0 0 24 24" fill="none" stroke="var(--rose)" stroke-width="2" stroke-linecap="round" stroke-linejoin="round" aria-hidden="true">
          <path d="M5 3h3l2 5-2 1.5a11 11 0 0 0 6.5 6.5L16 14l5 2v3a2 2 0 0 1-2 2A16 16 0 0 1 3 5a2 2 0 0 1 2-2z"/>
          <path d="M15 3a6 6 0 0 1 6 6M15 7a2 2 0 0 1 2 2"/>
        </svg>
      </li>
      <li class="contacts__item">mara@maraquillconsulting.com
        <svg class="contacts__icon" viewBox="0 0 24 24" fill="none" stroke="var(--rose)" stroke-width="2" stroke-linejoin="round" aria-hidden="true">
          <rect x="2" y="5" width="20" height="14" rx="1"/>
          <path d="M2 6l10 7 10-7"/>
        </svg>
      </li>
      <li class="contacts__item">www.maraquillconsulting.com
        <svg class="contacts__icon" viewBox="0 0 24 24" fill="none" stroke="var(--rose)" stroke-width="1.8" aria-hidden="true">
          <circle cx="12" cy="12" r="10"/>
          <ellipse cx="12" cy="12" rx="4.5" ry="10"/>
          <path d="M2 12h20M4 7h16M4 17h16"/>
        </svg>
      </li>
    </ul>
  </section>
</main>
</body>
</html>
```